Need simple and modern looking business card with all my information on one side and logo on the other side
Info :
Company name - VELMAR CONSTRUCTION LLC
Company addres- 418 harbor 87th. Dunmoor park ny 10352
Email- velmarllc@tridomail.Com
Company phone number 555-318-6094
Cell number- 555-742-0583
Web site - velmarllc.Com
My name Gerald tomasino

Target Market(s)

Construction , home improvement, remodeling

Industry/Entity Type

Construction

Contact Information for Business Card

It has to be moder but at the same time simple

Font styles to use
Sans Serif

Colors
0255a3
ffffff
000000
f78f20
b1b1b1
9d9d9d
1b1b1b
33a6d7
ec1f27

Requirements
Must have
• My logo on one side maybe with a some kind of background on the other side all my information
Nice to have
• Some kind of background pictures provided by you .PLEASE HAVE ACCOUNT WITH PIXELVAULT WILL NOT PAY ANY EXTRA FEES .
Should not have
• Any kind of hamer, nails,screws, helmets itp. Please do not copy the other designs come up with something new.

```html
<!DOCTYPE html>
<html lang="en">
<head>
<meta charset="utf-8">
<title>Velmar Construction LLC – Business Card</title>
<link rel="stylesheet" href="https://fonts.googleapis.com/css2?family=Open+Sans:wght@400;600&display=swap">
<style>
  :root {
    --canvas: #9d9d9d;
    --card-dark: #1b1b1b;
    --card-light: #ffffff;
    --ink: #000000;
    --ink-soft: #1b1b1b;
    --muted: #9d9d9d;
    --accent: #f78f20;
    --logo-text: #ffffff;
    --shadow: rgba(0, 0, 0, 0.35);
  }
  * { box-sizing: border-box; margin: 0; padding: 0; }
  html, body {
    width: 1200px;
    height: 900px;
    overflow: hidden;
  }
  body {
    background: var(--canvas);
    font-family: "Open Sans", Arial, sans-serif;
    position: relative;
  }
  .card {
    position: absolute;
    left: 285px;
    width: 630px;
    height: 360px;
    box-shadow: 0 10px 28px var(--shadow);
    overflow: hidden;
  }
  /* Front side: logo */
  .card--front {
    top: 70px;
    background: var(--card-dark);
  }
  .brand {
    position: absolute;
    left: 150px;
    top: 150px;
    display: flex;
    align-items: center;
    gap: 14px;
  }
  .brand__square {
    width: 22px;
    height: 22px;
    background: var(--accent);
  }
  .brand__name {
    color: var(--logo-text);
    font-weight: 600;
    font-size: 24px;
    letter-spacing: 3px;
    line-height: 1;
  }
  /* Back side: contact information */
  .card--back {
    top: 470px;
    background: var(--card-light);
    color: var(--ink-soft);
  }
  .accent-bar {
    position: absolute;
    left: 0;
    top: 150px;
    width: 215px;
    height: 14px;
    background: var(--accent);
  }
  .person {
    position: absolute;
    left: 232px;
    top: 104px;
  }
  .person__name {
    font-size: 30px;
    font-weight: 400;
    color: var(--ink);
    line-height: 1.1;
  }
  .person__title {
    font-size: 10px;
    letter-spacing: 5px;
    color: var(--muted);
    margin-top: 6px;
  }
  .contact {
    position: absolute;
    right: 34px;
    top: 38px;
    text-align: right;
    font-size: 14px;
    line-height: 1.45;
  }
  .address {
    position: absolute;
    left: 40px;
    top: 250px;
    font-size: 17px;
    line-height: 1.4;
    color: var(--ink);
  }
</style>
</head>
<body>
  <section class="card card--front" aria-label="Business card front">
    <div class="brand">
      <span class="brand__square"></span>
      <span class="brand__name">VELMAR CONSTRUCTION LLC</span>
    </div>
  </section>

  <section class="card card--back" aria-label="Business card back">
    <div class="contact">
      <p>Phone: 555-318-6094</p>
      <p>Cell number: 555-742-0583</p>
      <p>velmarllc@tridomail.com</p>
    </div>
    <div class="person">
      <p class="person__name">Gerald tomasino</p>
      <p class="person__title">MANAGING DIRECTOR</p>
    </div>
    <div class="accent-bar"></div>
    <address class="address" style="font-style: normal;">
      <p>418 harbor 87th.</p>
      <p>Dunmoor park ny 10352</p>
      <p>www.velmarllc.com</p>
    </address>
  </section>
</body>
</html>
```